New Business Card Design Project

I need a clean, professional business card. I'd like it to have some color, but not be wild. We do technology consulting and we have clients large and small who trust us with some of their most important data and projects. Simple but not boring should drive all design proposals. Multicolored and two sided, but with a matte finish, I think.
For more on tone, check out our website: http://quorvantis.example

Target Market(s)

Upper management of respected businesses. Tech savvy, but not "hipster".

Industry/Entity Type

Business

Requirements
Must have
• Files need to be provided in .eps and in .pdf in a manner that allows for easy updates.
Must have Name, Title, Phone, Email, Twitter, Website
Nice to have
• Logo/Name shouldn't be too big. One thing I've read several places is that the bigger the logo, the smaller the brand. A good article on dos and don'ts here: http://www.brindlepost.example/2011/02/business-card-experience.html

```html
<!DOCTYPE html>
<html lang="en">
<head>
<meta charset="utf-8">
<title>Quorvantis Business Card</title>
<link href="https://fonts.googleapis.com/css2?family=Dosis:wght@400;500&family=Questrial&display=swap" rel="stylesheet">
<style>
  :root {
    --backdrop: #e4e2dc;
    --card: #f7f8f7;
    --card-edge: #eaeeee;
    --ink: #7b7b7d;
    --ink-soft: #8a8a8c;
    --teal: #3f8a9c;
    --green: #8cb83a;
    --sky: #5ba8d6;
  }
  * { margin: 0; padding: 0; box-sizing: border-box; }
  html, body { width: 1200px; height: 900px; overflow: hidden; }
  body {
    background: var(--backdrop);
    position: relative;
    font-family: "Questrial", sans-serif;
    color: var(--ink);
  }
  .card {
    position: absolute;
    width: 664px;
    height: 383px;
    background: radial-gradient(ellipse at 50% 50%, #ffffff 0%, var(--card) 55%, var(--card-edge) 100%);
    border: 1px solid #d8dbda;
  }
  .card--front { left: 48px; top: 60px; }
  .card--back { left: 488px; top: 470px; }

  .brand {
    position: absolute;
    left: 0; right: 0; top: 160px;
    display: flex; align-items: center; justify-content: center; gap: 14px;
  }
  .brand__square { width: 16px; height: 16px; background: var(--teal); }
  .brand__name {
    font-size: 38px; letter-spacing: 2px; color: var(--ink);
  }

  .person {
    position: absolute; left: 0; right: 0; top: 102px;
    text-align: center;
    font-family: "Dosis", sans-serif;
  }
  .person__name {
    display: inline-flex; align-items: center; gap: 14px;
    font-size: 33px; font-weight: 500; letter-spacing: 2px; color: var(--ink);
  }
  .person__square { width: 12px; height: 12px; background: var(--teal); }
  .person__title {
    margin-top: 4px;
    font-size: 26px; font-weight: 500; letter-spacing: 2px; color: var(--ink);
  }

  .contacts {
    position: absolute; left: 30px; bottom: 28px;
    list-style: none; font-size: 19px; color: var(--ink-soft);
  }
  .contacts li { display: flex; align-items: center; gap: 12px; height: 25px; }
  .contacts svg { width: 20px; height: 18px; flex: none; }
  .phone {
    position: absolute; right: 34px; bottom: 28px;
    display: flex; align-items: center; gap: 12px; height: 25px;
    font-size: 19px; color: var(--ink-soft);
  }
  .phone svg { width: 16px; height: 22px; }
</style>
</head>
<body>

<section class="card card--front" aria-label="Card front">
  <div class="brand">
    <span class="brand__square" aria-hidden="true"></span>
    <span class="brand__name">QUORVANTIS</span>
  </div>
</section>

<section class="card card--back" aria-label="Card back">
  <div class="person">
    <div class="person__name"><span class="person__square" aria-hidden="true"></span>DANA WHITLOCK</div>
    <div class="person__title">CEO</div>
  </div>

  <ul class="contacts">
    <li>
      <svg viewBox="0 0 20 18" aria-hidden="true"><circle cx="10" cy="9" r="7" fill="var(--sky)"/></svg>
      quorvantist
    </li>
    <li>
      <svg viewBox="0 0 20 18" aria-hidden="true">
        <circle cx="10" cy="9" r="7.5" fill="none" stroke="var(--ink)" stroke-width="1.8"/>
        <ellipse cx="10" cy="9" rx="3.2" ry="7.5" fill="none" stroke="var(--ink)" stroke-width="1.4"/>
        <line x1="2.5" y1="9" x2="17.5" y2="9" stroke="var(--ink)" stroke-width="1.4"/>
      </svg>
      www.quorvantis.example
    </li>
    <li>
      <svg viewBox="0 0 20 18" aria-hidden="true">
        <rect x="1" y="3" width="18" height="12" fill="var(--green)"/>
        <polyline points="1,3 10,10 19,3" fill="none" stroke="#ffffff" stroke-width="1.5"/>
      </svg>
      dana@quorvantis.example
    </li>
  </ul>

  <div class="phone">
    <svg viewBox="0 0 16 22" aria-hidden="true">
      <rect x="1" y="1" width="14" height="20" rx="2" fill="none" stroke="var(--ink)" stroke-width="1.8"/>
      <line x1="1" y1="16" x2="15" y2="16" stroke="var(--ink)" stroke-width="1.4"/>
    </svg>
    1-800-555-0142, ext. 700
  </div>
</section>

</body>
</html>
```